Wordpress 6 pages GLAM design for hair salon

Hi guys.
I need a glam & easy to navigate web design for my (women only) new hair salon.
I have a logo. You can see in attached files.
I like 3d backgrounds.
My favourite colours choice: any variety of pink(hot & very soft), white, black, grey.
I would like to see website very feminine, glamorous & kind of old Hollywood and Doreen Valcourt inspired.
Of course it should have plug ins, like social media, map, security etc.
My website now: http://velorimtresses.example

Designs what I like:
http://quarnetsalon.example
http://lumbrivespastudio.example
http://www.tindrelgraphicdesign.example/boutique-graphic-web-folio.html

Target Market(s)

WOMEN

Industry/Entity Type

Boutique

Requirements
Should not have
• any cartoon or other characters!

```html
<!DOCTYPE html>
<html lang="en">
<head>
<meta charset="utf-8">
<title>Velorim Tresses – Hair Salon</title>
<link href="https://fonts.googleapis.com/css2?family=Signika:wght@300;400;600&display=swap" rel="stylesheet">
<style>
:root{
  --pink:#d0577f;
  --pink-light:#dd7c9c;
  --pink-text:#c9456f;
  --bg-soft:#efd3e0;
  --bg-deep:#d9a8c0;
  --page:#f7f7f7;
  --panel:#ececec;
  --dark:#2c2c2c;
  --dark-2:#3e3e3e;
  --text:#666;
  --line:#d6d6d6;
}
*{box-sizing:border-box;margin:0;padding:0}
html,body{width:1034px;height:1200px;overflow:hidden}
body{font-family:'Signika',sans-serif;position:relative;color:var(--text)}
.backdrop{position:absolute;inset:0;background:radial-gradient(circle at 50% 50%,var(--bg-soft) 0%,var(--bg-deep) 100%)}
.page{position:absolute;left:103px;top:32px;width:827px;height:1136px;background:var(--page);box-shadow:0 0 6px rgba(0,0,0,.15)}
.brand{position:absolute;left:24px;top:38px;display:flex;align-items:center;gap:8px}
.brand-dot{width:14px;height:14px;border-radius:50%;background:var(--pink)}
.brand-name{font-size:22px;font-weight:400;color:var(--pink-text)}
.follow{position:absolute;right:18px;top:50px;display:flex;align-items:center;gap:10px;font-size:12px;color:var(--pink-text)}
.follow .dot{width:20px;height:20px;border-radius:50%;background:#8a8a8a}
.nav{position:absolute;left:9px;top:116px;width:810px;height:40px;background:linear-gradient(#4a4a4a,#262626);display:flex;align-items:center}
.nav a{color:#fff;text-decoration:none;font-size:12px;text-transform:uppercase}
.nav-links{display:flex;margin-left:27px}
.nav-links a{margin-right:0}
.search{position:absolute;right:18px;top:7px;width:180px;height:27px;background:#fff;border-radius:2px}
.search svg{position:absolute;right:8px;top:6px}
.hero{position:absolute;left:9px;top:164px;width:810px;height:291px;background:radial-gradient(ellipse at 20% 40%,#8a5a40 0%,#4a2a1e 45%,#2a1812 100%)}
.hero-arrows{position:absolute;right:22px;bottom:16px}
.welcome{position:absolute;left:9px;top:485px;width:534px;height:265px;background:var(--panel)}
.band{height:39px;background:linear-gradient(var(--pink-light),var(--pink));color:#fff;font-size:19px;padding:11px 18px 0;}
.welcome p{font-size:11.2px;line-height:17px;padding:0 18px;margin-top:17px}
.welcome p+p{margin-top:21px}
.btn{display:inline-block;background:linear-gradient(#444,#222);color:#fff;font-size:11.5px;padding:6px 18px;border-radius:2px}
.welcome .btn{position:absolute;left:18px;top:223px;height:27px}
.calendar{position:absolute;left:559px;top:486px;width:260px}
.cal-head{height:39px;background:linear-gradient(#4a4a4a,#262626);color:#fff;text-align:center;font-size:15px;padding-top:11px}
.cal-body{background:#e9e9e9;height:193px;margin-top:2px;padding:16px 40px 0}
.cal-body table{width:100%;border-collapse:collapse;font-size:9px;color:#333;text-align:center}
.cal-body th{font-size:14px;font-weight:600;color:#333;padding-bottom:6px;border-bottom:1px solid var(--line)}
.cal-body td{height:24px}
.cal-body tr:last-child td{border-bottom:1px solid var(--line)}
.cal-nav{display:flex;justify-content:space-between;font-size:11px;color:var(--pink-text);margin-top:18px;border-bottom:1px dotted #ccc;height:10px}
.cal-nav span{background:var(--page);padding-right:2px}
.cal-nav span+span{padding:0 0 0 2px}
.recent{position:absolute;left:9px;top:778px;width:810px;height:223px;background:var(--panel)}
.recent .band{font-size:17px;padding-left:14px}
.post{position:absolute;top:59px;width:246px}
.post-date{font-size:11px;font-weight:600;color:var(--pink-text);padding-bottom:8px;border-bottom:1px solid var(--line)}
.post p{font-size:11.2px;line-height:17px;margin-top:12px}
.post .btn{position:absolute;top:124px;left:1px;width:66px;height:25px;text-align:center;padding:5px 0}
.footer{position:absolute;left:0;bottom:0;width:827px;height:104px;background:linear-gradient(#3a3a3a,#2a2a2a)}
.foot-links{position:absolute;left:18px;top:26px;display:flex;gap:16px;font-size:11px;color:#e6e6e6;text-transform:uppercase}
.copy{position:absolute;left:18px;top:53px;font-size:11.5px;color:#e6e6e6}
.foot-follow{position:absolute;right:30px;top:32px;display:flex;align-items:center;gap:16px;color:#e6e6e6;font-size:12px}
.foot-follow .dot{width:24px;height:24px;border-radius:50%;background:#fff}
</style>
</head>
<body>
<div class="backdrop" role="img" aria-label="Soft pink tufted quilted background"></div>
<div class="page">
  <div class="brand"><span class="brand-dot"></span><span class="brand-name">Velorim Tresses</span></div>
  <div class="follow">Follow Us : <span class="dot"></span><span class="dot"></span><span class="dot"></span></div>

  <nav class="nav">
    <div class="nav-links">
      <a href="#" style="margin-right:37px">Home</a>
      <a href="#" style="margin-right:44px">About Us</a>
      <a href="#" style="margin-right:47px">Services</a>
      <a href="#" style="margin-right:54px">Gallery</a>
      <a href="#" style="margin-right:52px">Blog</a>
      <a href="#">Contacts</a>
    </div>
    <div class="search">
      <svg width="15" height="15" viewBox="0 0 15 15"><circle cx="6" cy="6" r="4.5" fill="none" stroke="#c9456f" stroke-width="2"/><line x1="9.3" y1="9.3" x2="13.5" y2="13.5" stroke="#c9456f" stroke-width="2.4" stroke-linecap="round"/></svg>
    </div>
  </nav>

  <div class="hero" role="img" aria-label="Photo of a woman with long glossy brown wavy hair">
    <svg class="hero-arrows" width="26" height="16" viewBox="0 0 26 16"><polyline points="8,2 2,8 8,14" fill="none" stroke="#fff" stroke-width="2"/><polyline points="18,2 24,8 18,14" fill="none" stroke="#fff" stroke-width="2"/></svg>
  </div>

  <section class="welcome">
    <div class="band">Welcome To Our Website!</div>
    <p>Our salon is based on the belief that our customers' needs are of the utmost importance. Our team is committed to meeting those needs. As a result, a high percentage of our business is from repeat customers and referrals.</p>
    <p>We would welcome the opportunity to earn your trust and deliver you the best service in the industry! A professional stylist/colorist is fundamentally different from the classic hairdresser. The name of the profession comes from the word” color”, because the colorist specializes in hair coloring. Moreover, the procedure of dying with colorist has an independent.</p>
    <span class="btn">Learn More</span>
  </section>

  <aside class="calendar">
    <div class="cal-head">January 2014</div>
    <div class="cal-body">
      <table>
        <tr><th>S</th><th>M</th><th>T</th><th>W</th><th>T</th><th>F</th><th>S</th></tr>
        <tr><td></td><td></td><td></td><td>1</td><td>2</td><td>3</td><td>4</td></tr>
        <tr><td>5</td><td>6</td><td>7</td><td>8</td><td>9</td><td>10</td><td>11</td></tr>
        <tr><td>12</td><td>13</td><td>14</td><td>15</td><td>16</td><td>17</td><td>18</td></tr>
        <tr><td>19</td><td>20</td><td>21</td><td>22</td><td>23</td><td>24</td><td>25</td></tr>
        <tr><td>26</td><td>27</td><td>28</td><td>29</td><td>30</td><td>31</td><td></td></tr>
      </table>
    </div>
    <div class="cal-nav"><span>&lt;&lt; Previous</span><span>Next &gt;&gt;</span></div>
  </aside>

  <section class="recent">
    <div class="band">Recent Post</div>
    <article class="post" style="left:13px">
      <div class="post-date">JANUARY 6, 2014</div>
      <p>by Dr.L There is too much hairspray on the shelf if you go to the We would welcome the opportunity to earn your trust and deliver you the best service in the industry...</p>
      <span class="btn">More</span>
    </article>
    <article class="post" style="left:277px">
      <div class="post-date">JANUARY 6, 2014</div>
      <p>by Dr.L There is too much hairspray on the shelf if you go to the We would welcome the opportunity to earn your trust and deliver you the best service in the industry...</p>
      <span class="btn">More</span>
    </article>
    <article class="post" style="left:552px">
      <div class="post-date">JANUARY 6, 2014</div>
      <p>by Dr.L There is too much hairspray on the shelf if you go to the We would welcome the opportunity to earn your trust and deliver you the best service in the industry...</p>
      <span class="btn">More</span>
    </article>
  </section>

  <footer class="footer">
    <div class="foot-links"><span>Home</span><span>About Us</span><span>Services</span><span>Gallery</span><span>Blog</span><span>Contacts</span></div>
    <div class="copy">Velorim Hair Studio © 2014 | Privacy Policy</div>
    <div class="foot-follow">Follow Us : <span class="dot"></span><span class="dot"></span></div>
  </footer>
</div>
</body>
</html>
```